Valto Sàrl - Business Card

VALTO Sàrl operates in the sector Services for banks and credit institutions. It is a B2B which connects companies. The main colors should be Blue and Black. The logo and look of the card should be simple, professional, conservative and reflect Connecting People.

Target Market(s)

Financial professionals and institutions

Industry/Entity Type

Finance

Contact Information for Business Card

Chemin des Prés 9
1027 Lonay

Logo Text

Connecting dots

Font styles to use
Serif
Sans Serif

Colors
0355a3
3176b5
85acd3
cfdeed

Requirements
Should not have
• Multiple colors

```html
<!DOCTYPE html>
<html lang="fr">
<head>
<meta charset="utf-8">
<title>Valto Sàrl – Business Card</title>
<link rel="stylesheet" href="https://fonts.googleapis.com/css2?family=Alegreya:wght@500&family=Mulish:wght@300;400&display=swap">
<style>
  :root {
    --backdrop: #b3b2ad;
    --card: #222223;
    --accent: #45aee6;
    --ink: #ffffff;
  }
  * { margin: 0; padding: 0; box-sizing: border-box; }
  html, body {
    width: 1200px;
    height: 1200px;
    overflow: hidden;
    background: var(--backdrop);
  }
  .sheet {
    position: relative;
    width: 1200px;
    height: 1200px;
    display: flex;
    align-items: center;
    justify-content: center;
    gap: 80px;
  }
  .card {
    position: relative;
    width: 420px;
    height: 650px;
    background: var(--card);
    box-shadow: 0 10px 30px rgba(0, 0, 0, 0.18);
  }
  .accent-bar {
    position: absolute;
    left: 50%;
    width: 190px;
    height: 44px;
    margin-left: -95px;
    background: var(--accent);
  }
  .accent-bar--top { top: 0; }
  .accent-bar--bottom { bottom: 0; }

  .brand {
    position: absolute;
    top: 200px;
    left: 0;
    width: 100%;
    display: flex;
    flex-direction: column;
    align-items: center;
  }
  .brand__dot {
    width: 70px;
    height: 70px;
    border-radius: 50%;
    background: var(--accent);
    margin-bottom: 38px;
  }
  .brand__name {
    font-family: "Alegreya", Georgia, serif;
    font-weight: 500;
    font-size: 54px;
    letter-spacing: 2px;
    color: var(--ink);
    line-height: 1;
  }

  .address {
    position: absolute;
    left: 80px;
    bottom: 110px;
    display: flex;
    align-items: center;
    gap: 18px;
    font-family: "Mulish", Arial, sans-serif;
    font-style: normal;
    font-weight: 300;
    font-size: 24px;
    line-height: 1.2;
    color: var(--ink);
  }
  .address__pin { width: 26px; height: 38px; flex: none; }

  .card--back .address {
    bottom: 80px;
    font-size: 20px;
  }
</style>
</head>
<body>
  <main class="sheet">
    <section class="card card--front">
      <div class="accent-bar accent-bar--top"></div>
      <div class="brand">
        <div class="brand__dot"></div>
        <div class="brand__name">VALTO Sàrl</div>
      </div>
      <address class="address">
        <svg class="address__pin" viewBox="0 0 26 38" aria-hidden="true">
          <path d="M13 0C5.8 0 0 5.8 0 13c0 9.5 13 25 13 25s13-15.5 13-25C26 5.8 20.2 0 13 0z" fill="#ffffff"/>
          <circle cx="13" cy="12.5" r="5" fill="#222223"/>
        </svg>
        <span>Chemin des Prés 9<br>1027 Lonay</span>
      </address>
      <div class="accent-bar accent-bar--bottom"></div>
    </section>

    <section class="card card--back">
      <address class="address">
        <svg class="address__pin" viewBox="0 0 26 38" aria-hidden="true">
          <path d="M13 0C5.8 0 0 5.8 0 13c0 9.5 13 25 13 25s13-15.5 13-25C26 5.8 20.2 0 13 0z" fill="#ffffff"/>
          <circle cx="13" cy="12.5" r="5" fill="#222223"/>
        </svg>
        <span>Chemin des Prés 9<br>1027 Lonay</span>
      </address>
      <div class="accent-bar accent-bar--bottom"></div>
    </section>
  </main>
</body>
</html>
```